Holiday Rental Leaflet

Want a DL size double sided leaflet to distribute via local businesses, markets, family and friends
HOLIDAY RENTALCarrickalinga - 17 Farrow Street Sleeps 8-10 (2 Queen, 1 Double, 2 bunks), 4 bedrooms, BIR to all bedrooms 2 Bathrooms, one with bath, 2 toilets Open Plan Lounge/Dining/Kitchen area Dining Table for 8 peopleReverse cycle airconditionerSlow combustion wood heaterTV/DVD, CD/RadioKitchen has m/wave, oven, fridge/freezer, dishwasherBBQ providedTimber decking with 2 outside tables and 12 chairs Washing Machine and dryer provided One street back from beach Smoke free zone No Pets
For further information or to book contact Joan on 0491 278 306 or email joanbirch62@veltranet.com.au

Requirements
Nice to have
• Have sent a variety of photos of the house. No need to use all of them, pick out the most relevant for the leaflet.

```html
<!DOCTYPE html>
<html lang="en">
<head>
<meta charset="utf-8">
<title>Holiday Rental Carrickalinga – Leaflet</title>
<link href="https://fonts.googleapis.com/css2?family=Baumans&family=Lato:wght@400;700;900&family=Roboto+Condensed:wght@700&display=swap" rel="stylesheet">
<style>
  :root{
    --page:#2b2b2b;
    --red:#d8441d;
    --yellow:#ecaf10;
    --white:#ffffff;
    --ink:#555555;
    --sky:#8fb4d0;
    --sea:#3f7ea8;
    --green:#5f7a3c;
  }
  *{box-sizing:border-box;margin:0;padding:0}
  html,body{width:806px;height:1200px;overflow:hidden;background:var(--page)}
  .leaflet{position:absolute;left:131px;top:90px;width:544px;height:1020px;overflow:hidden;font-family:"Lato",sans-serif}
  .leaflet-bg{position:absolute;inset:0}
  .hero-photo{position:absolute;left:0;top:0;width:544px;height:290px;
    background:linear-gradient(180deg,var(--sky) 0%,#6f9cc0 20%,var(--sea) 38%,#7d8f5a 58%,var(--green) 100%)}
  .title{position:absolute;left:0;right:0;top:24px;text-align:center;color:var(--white);
    font-family:"Baumans",sans-serif;font-size:28px;font-weight:400;letter-spacing:.4px;line-height:1}
  .address{position:absolute;left:0;right:0;top:55px;text-align:center;color:var(--white);
    font-weight:400;font-size:22px;letter-spacing:.5px;line-height:28px}
  .feature-card{position:absolute;top:134px;width:142px;height:254px}
  .feature-card .card-body{position:absolute;left:0;right:0;top:30px;bottom:0;background:var(--yellow);
    border:5px solid var(--white);border-radius:30px}
  .feature-card .card-photo{position:absolute;left:22px;top:0;width:98px;height:98px;border-radius:50%;
    background:var(--yellow);border:5px solid var(--white)}
  .feature-card .card-photo span{position:absolute;inset:5px;border-radius:50%}
  .card-text{position:absolute;left:8px;right:8px;top:106px;color:var(--white);text-align:center;
    font-size:9.2px;font-weight:700;line-height:12.6px}
  .card-bedroom{left:51px}.card-bedroom .card-photo span{background:linear-gradient(135deg,#a9694a,#4a68b8)}
  .card-bathroom{left:198px}.card-bathroom .card-photo span{background:linear-gradient(135deg,#e6e6e6,#b7b2aa)}
  .card-beach{left:346px}.card-beach .card-photo span{background:linear-gradient(180deg,#8fb3d4,#4d87b0 45%,#d8c9a6 60%,#b8a47e)}
  .amenities{position:absolute;left:50px;width:442px;top:427px;text-align:right;color:var(--white);
    font-size:16.4px;font-weight:700;line-height:22.2px}
  .cyclist-photo{position:absolute;left:52px;top:622px;width:127px;height:318px;border-radius:40px 40px 20px 20px;
    background:linear-gradient(180deg,#3c3c3c 0%,#e0701f 20%,#d9651c 38%,#2c2c2c 55%,#5a5a5a 100%)}
  .contact-tab{position:absolute;left:198px;top:656px;width:346px;height:60px;background:var(--white);border-radius:18px 0 0 0}
  .contact-line{position:absolute;left:212px;top:669px;font-family:"Roboto Condensed",sans-serif;font-weight:700;
    font-size:27px;line-height:32px;white-space:nowrap;display:flex;align-items:center}
  .contact-name{color:var(--yellow)}
  .contact-phone{color:var(--red)}
  .phone-icon{width:22px;height:24px;margin:0 4px 0 7px}
  .blurb{position:absolute;right:52px;width:320px;top:714px;text-align:right;color:var(--ink);
    font-size:15.8px;font-weight:700;line-height:23px;white-space:nowrap}
  .email{position:absolute;left:56px;top:940px;display:flex;align-items:center;color:var(--white);
    font-size:25px;font-weight:700;line-height:32px}
  .globe{width:26px;height:26px;margin-right:10px}
</style>
</head>
<body>
<main class="leaflet">
  <div class="hero-photo" role="img" aria-label="Coastal view of the sea over the rental house roof and garden hedges"></div>
  <svg class="leaflet-bg" width="544" height="1020" viewBox="0 0 544 1020" aria-hidden="true">
    <defs>
      <linearGradient id="redFill" x1="0" y1="0" x2="0" y2="1">
        <stop offset="0" stop-color="#e04a1f"/><stop offset="1" stop-color="#cc3c1b"/>
      </linearGradient>
    </defs>
    <path d="M0 258 C120 232 250 268 360 246 C440 232 500 222 544 226 L544 800 L0 800 Z" fill="url(#redFill)"/>
    <path d="M0 712 C150 682 320 664 544 656 L544 1020 L0 1020 Z" fill="var(--white)"/>
    <path d="M0 910 C50 882 110 906 190 896 C290 882 370 906 450 886 C495 876 525 886 544 882 L544 1020 L0 1020 Z" fill="var(--yellow)"/>
  </svg>

  <h1 class="title">HOLIDAY RENTAL CARRICKALINGA</h1>
  <p class="address">17 Farrow Street</p>

  <section class="feature-card card-bedroom">
    <div class="card-body"></div>
    <div class="card-photo"><span role="img" aria-label="Bedroom with colourful bedding"></span></div>
    <p class="card-text">Lorem Ipsum is simply<br>dummy text of the<br>printing and typesetting<br>industry. Lorem Ipsum has<br>been the industry's<br>standard dummy text ever<br>since the 1500s, when an<br>unknown printer took a<br>galley of type and<br>scrambled it to make a<br>type specimen book.</p>
  </section>
  <section class="feature-card card-bathroom">
    <div class="card-body"></div>
    <div class="card-photo"><span role="img" aria-label="White bathroom with bath"></span></div>
    <p class="card-text">Lorem Ipsum is simply<br>dummy text of the<br>printing and typesetting<br>industry. Lorem Ipsum has<br>been the industry's<br>standard dummy text ever<br>since the 1500s, when an<br>unknown printer took a<br>galley of type and<br>scrambled it to make a<br>type specimen book.</p>
  </section>
  <section class="feature-card card-beach">
    <div class="card-body"></div>
    <div class="card-photo"><span role="img" aria-label="Nearby sandy beach and sea"></span></div>
    <p class="card-text">Lorem Ipsum is simply<br>dummy text of the<br>printing and typesetting<br>industry. Lorem Ipsum has<br>been the industry's<br>standard dummy text ever<br>since the 1500s, when an<br>unknown printer took a<br>galley of type and<br>scrambled it to make a<br>type specimen book.</p>
  </section>

  <p class="amenities">2 Queen, 1 Double, 2 bunks, 4 bedrooms, BIR to all<br>bedrooms 2 Bathrooms, one with bath, 2 toilets Open<br>Plan Lounge/Dining/Kitchen area Dining Table for 8<br>peopleReverse cycle airconditionerSlow combustion<br>wood heaterTV/DVD, CD/RadioKitchen has m/wave,<br>oven, fridge/freezer, &nbsp;dishwasherBBQ providedTimber<br>decking with 2 outside tables and 12 chairs Washing<br>Machine and dryer provided One street back from<br>beach Smoke free zone No Pets</p>

  <div class="contact-tab"></div>
  <p class="contact-line">
    <span class="contact-name">Joan on</span>
    <svg class="phone-icon" viewBox="0 0 22 24" aria-hidden="true">
      <rect x="0" y="0" width="22" height="24" rx="4" fill="var(--red)"/>
      <path d="M7 5 C5 6 4 8 5 11 C6 14 9 18 13 19 C15 20 16 19 17 17 L14.5 14.5 L12.5 15.5 C10.5 14 9 12 8.5 10 L10 8.5 Z" fill="var(--white)"/>
    </svg>
    <span class="contact-phone">0491 278 306</span>
  </p>

  <div class="cyclist-photo" role="img" aria-label="Cyclist in an orange jacket riding a mountain bike"></div>

  <p class="blurb">Lorem Ipsum is simply dummy text of<br>the printing and typesetting industry.<br>Lorem Ipsum has been the industry's<br>standard dummy text ever since the<br>1500s, when an unknown printer took a<br>galley of type and scrambled it to make<br>a type specimen book.</p>

  <p class="email">
    <svg class="globe" viewBox="0 0 26 26" aria-hidden="true" fill="none" stroke="var(--white)" stroke-width="2">
      <circle cx="13" cy="13" r="11"/><ellipse cx="13" cy="13" rx="5" ry="11"/>
      <line x1="2" y1="13" x2="24" y2="13"/><path d="M4 7 H22 M4 19 H22"/>
    </svg>
    joanbirch62@veltranet.com.au
  </p>
</main>
</body>
</html>
```